Stationary Design (using existing logo)

Stationary (print and electronic version for Word/email), envelope, and fax cover. All companies are part of same family or course so designs can be the same, or essentially the same. Use the logos attached, same font and colors.

Target Market(s)

Real estate professionals. Investors and other property owners. Financial professionals.

Industry/Entity Type

Real Estate

Font styles to use
Serif

Requirements
Must have
• Should be a serious, sophisticated design in colors that match the business cards we uploaded. Design needs to match the color and fonts in the attached business cards. Can use the same design for each company, just change logo and color.
Should not have
• Nothing quirky or cute.

```html
<!DOCTYPE html>
<html lang="en">
<head>
<meta charset="utf-8">
<title>KVL Restoration Services – Stationery</title>
<link href="https://fonts.googleapis.com/css2?family=Questrial&family=Arimo:wght@400;700&display=swap" rel="stylesheet">
<style>
  :root{
    --green:#035a4e;
    --green-dark:#024a40;
    --bronze:#8a7560;
    --bronze-light:#c9b8a3;
    --paper:#f4f4f4;
    --ink:#222;
    --rule:#777;
    --bg:#d9d9d9;
  }
  *{box-sizing:border-box;margin:0;padding:0}
  html,body{width:1200px;height:1000px;overflow:hidden}
  body{background:var(--bg);font-family:"Questrial",sans-serif;color:var(--ink);position:relative}
  .sheet{position:absolute;background:var(--paper);overflow:hidden}
  .brand{position:absolute;display:flex;align-items:center;gap:5px;color:var(--green);font-family:"Questrial",sans-serif;white-space:nowrap}
  .brand-mark{width:9px;height:9px;background:var(--green)}
  .brand-name{font-size:13px;letter-spacing:.5px}
  .band{position:absolute;left:0;right:0;bottom:0}
  .band-line{height:7px;background:linear-gradient(90deg,var(--bronze) 0%,var(--bronze-light) 45%,#e8f0ee 55%,var(--bronze-light) 65%,var(--bronze) 100%)}
  .band-bar{height:17px;background:var(--green);color:#fff;font-size:6.2px;display:flex;align-items:center;justify-content:center;white-space:nowrap}
  .band-bar b{font-weight:700;font-family:"Arimo",sans-serif;margin:0 2px}

  /* letterhead */
  .letterhead{left:166px;top:61px;width:417px;height:539px}
  .letterhead .brand{left:50%;top:42px;transform:translateX(-50%)}
  .letter-body{position:absolute;left:38px;top:171px;width:342px;font-size:6.3px;line-height:7.4px;color:#333}
  .letter-body p{margin-bottom:7px}
  .letter-body .salutation{font-family:"Arimo",sans-serif;font-weight:700;margin-bottom:7px}
  .sign-off{margin-top:10px;display:flex;align-items:flex-start;gap:8px}
  .sign-off strong{font-family:"Arimo",sans-serif}
  .signature{width:86px;height:42px;background:linear-gradient(90deg,#e6e9f3,#dfe4f2);border-radius:3px}

  /* fax */
  .fax{left:616px;top:61px;width:417px;height:539px}
  .fax .brand{left:38px;top:42px}
  .fax-title{position:absolute;right:38px;top:22px;font-family:"Arimo",sans-serif;font-size:48px;color:#4a4a4a;letter-spacing:1px}
  .fax-fields{position:absolute;left:38px;top:97px;width:341px;border-collapse:collapse;font-family:"Arimo",sans-serif;font-size:5.8px;font-weight:700}
  .fax-fields td{border:1px solid var(--rule);height:12.2px;padding:0 3px}
  .fax-fields .label{width:36px}
  .fax-fields .label-r{width:36px}
  .fax-status{position:absolute;left:38px;top:170px;width:341px;height:12px;display:flex;background:#e4e4e4;border:1px solid var(--rule);font-family:"Arimo",sans-serif;font-size:5.6px}
  .fax-status span{flex:1;display:flex;align-items:center;justify-content:center;gap:3px;border-right:1px solid var(--rule)}
  .fax-status span:last-child{border-right:none}
  .fax-status i{display:inline-block;width:4px;height:4px;border:1px solid #666}
  .fax-comments{position:absolute;left:38px;top:182px;width:341px;height:313px;border:1px solid var(--rule);border-top:none;font-family:"Arimo",sans-serif;font-size:6px;text-align:center;padding-top:11px;color:#333}

  /* envelopes */
  .envelope-front{left:117px;top:630px;width:465px;height:201px}
  .envelope-front .brand{left:24px;top:40px}
  .envelope-back{left:616px;top:630px;width:466px;height:201px}
  .envelope-flap{position:absolute;left:0;top:0}
  .return-address{position:absolute;left:0;right:0;top:28px;text-align:center;color:#fff;font-size:5.8px;line-height:7px}

  /* business cards */
  .card-front{left:410px;top:861px;width:172px;height:99px;background:var(--green)}
  .card-front .brand{left:50%;top:40px;transform:translateX(-50%);color:#fff}
  .card-front .brand-mark{background:#fff}
  .card-front .brand-name{font-size:10px}
  .card-url{position:absolute;left:0;right:0;top:80px;text-align:center;color:#fff;font-size:4.5px}
  .card-back{left:616px;top:861px;width:172px;height:99px}
  .card-back .brand{left:50%;top:16px;transform:translateX(-50%)}
  .card-back .brand-name{font-size:10px}
  .card-name{position:absolute;left:0;right:0;top:55px;text-align:center;color:var(--green);font-family:"Arimo",sans-serif;font-weight:700;font-size:5.5px}
  .card-name small{font-weight:400;font-size:4px}
  .card-role{position:absolute;left:0;right:0;top:62px;text-align:center;font-size:3.8px;color:#444}
  .card-contact{position:absolute;left:0;right:0;top:72px;text-align:center;font-size:3.8px;color:var(--green)}
  .card-back .band-line{height:4px}
  .card-back .band-bar{height:11px;font-size:4px}
</style>
</head>
<body>

<section class="sheet letterhead">
  <div class="brand"><span class="brand-mark"></span><span class="brand-name">KVL Restoration Services</span></div>
  <div class="letter-body">
    <p class="salutation">Dear sir,</p>
    <p>Thank you for the time you gave us last week. We have reviewed the property and prepared a full scope of work covering the roof, the facade and the interior finishes. Our team can begin within two weeks of approval, and every phase will be documented and shared with you.</p>
    <p>The enclosed estimate lists each item with its cost and expected duration. Where insurance coverage applies, we will coordinate directly with your adjuster so that claims move forward without delay. Materials are sourced from trusted suppliers and match the original character of the building wherever possible.</p>
    <p>We understand that each property is an investment, and we treat it with the same care we would give our own. Should any question arise during the work, your project manager will be available by phone or email.</p>
    <p>Please review the proposal at your convenience and let us know how you wish to proceed. We look forward to working with you.</p>
    <div class="sign-off">
      <div>Yours Sincerely,<br><strong>Dana Whitlock</strong></div>
      <div class="signature" role="img" aria-label="Handwritten signature in blue ink"></div>
    </div>
  </div>
  <footer class="band">
    <div class="band-line"></div>
    <div class="band-bar">1418 N Larchmont Ave., Evanston, IL 60201 · <b>Phone:</b> 312.555.0148 · <b>Email:</b> info@kvlrealty.com · www.<b>kvlrealty</b>.com</div>
  </footer>
</section>

<section class="sheet fax">
  <div class="brand"><span class="brand-mark"></span><span class="brand-name">KVL Restoration Services</span></div>
  <div class="fax-title">FAX</div>
  <table class="fax-fields">
    <tr><td class="label">To:</td><td></td><td class="label-r">From:</td><td></td></tr>
    <tr><td class="label">Fax:</td><td></td><td class="label-r">Pages:</td><td></td></tr>
    <tr><td class="label">Phone:</td><td></td><td class="label-r">Date:</td><td></td></tr>
    <tr><td class="label">Re:</td><td></td><td class="label-r">CC:</td><td></td></tr>
  </table>
  <div class="fax-status">
    <span><i></i>Urgent</span><span><i></i>For Review</span><span><i></i>Please Comment</span><span><i></i>Please Reply</span><span><i></i>Please Recycle</span>
  </div>
  <div class="fax-comments">COMMENTS:</div>
  <footer class="band">
    <div class="band-line"></div>
    <div class="band-bar">1418 N Larchmont Ave., Evanston, IL 60201 · <b>Phone:</b> 312.555.0148 · <b>Email:</b> info@kvlrealty.com · www.<b>kvlrealty</b>.com</div>
  </footer>
</section>

<section class="sheet envelope-front">
  <div class="brand"><span class="brand-mark"></span><span class="brand-name">KVL Restoration Services</span></div>
  <footer class="band">
    <div class="band-line" style="height:5px"></div>
    <div class="band-bar" style="height:8px"></div>
  </footer>
</section>

<section class="sheet envelope-back">
  <svg class="envelope-flap" width="466" height="68" viewBox="0 0 466 68" aria-hidden="true">
    <path d="M0 0 H466 L450 62 Q448 68 441 68 H25 Q18 68 16 62 Z" fill="var(--green)"/>
  </svg>
  <div class="return-address">1418 N Larchmont Ave.<br>Evanston, IL 60201</div>
</section>

<section class="sheet card-front">
  <div class="brand"><span class="brand-mark" style="width:7px;height:7px"></span><span class="brand-name">KVL Restoration Services</span></div>
  <div class="card-url">www.kvlrealty.com</div>
</section>

<section class="sheet card-back">
  <div class="brand"><span class="brand-mark" style="width:7px;height:7px"></span><span class="brand-name">KVL Restoration Services</span></div>
  <div class="card-name">R. Paul Lindqvist, <small>Esq</small></div>
  <div class="card-role">Managing Broker</div>
  <div class="card-contact"><b>P:</b> 312.555.0148 <b>E:</b> info@kvlrealty.com · www.kvlrealty.com</div>
  <footer class="band">
    <div class="band-line"></div>
    <div class="band-bar">1418 N Larchmont Ave., Evanston, IL 60201</div>
  </footer>
</section>

</body>
</html>
```